Water vending machine graphic

To create a front graphic for a water vending machine
Name of water is Cedar Hollow

Target Market(s)

general population

Requirements
Must have
• Water picture, bottles, person drinking water

```html
<!DOCTYPE html>
<html lang="en">
<head>
<meta charset="utf-8">
<title>Cedar Hollow – Vending Machine Graphics</title>
<link rel="stylesheet" href="https://fonts.googleapis.com/css2?family=Cinzel:wght@700&family=Montserrat:ital,wght@0,700;0,800;0,900;1,800;1,900&family=Arimo:wght@400;700&display=swap">
<style>
  :root{
    --page-top:#f4f4f4;
    --page-bottom:#e9e9e9;
    --label-grey:#b7b7b7;
    --blue-deep:#0b53ab;
    --blue:#1f7fd2;
    --blue-mid:#3a9be3;
    --sky:#8fd4f1;
    --navy:#17439a;
    --brand-blue:#1260b8;
    --ink:#111111;
    --white:#ffffff;
  }
  *{box-sizing:border-box;margin:0;padding:0}
  html,body{width:1000px;height:1200px;overflow:hidden}
  body{
    background:linear-gradient(180deg,var(--page-top),var(--page-bottom));
    font-family:"Arimo",Arial,sans-serif;
    position:relative;
  }
  .view-label{
    position:absolute;top:90px;
    font-family:"Cinzel",serif;font-weight:700;font-size:32px;
    letter-spacing:3px;color:var(--label-grey);
  }
  .view-label--front{left:162px}
  .view-label--side{left:594px}

  .panel{position:absolute;top:175px;height:972px;overflow:hidden;background:var(--blue)}
  .panel--front{left:111px;width:389px}
  .panel--side{left:574px;width:304px}
  .panel-art{position:absolute;inset:0;width:100%;height:100%}
  .panel > *:not(.panel-art){position:absolute}

  .brand{text-align:center;color:var(--brand-blue)}
  .brand-name{
    font-family:"Montserrat",sans-serif;font-weight:800;
    display:flex;align-items:center;justify-content:center;gap:6px;white-space:nowrap;
  }
  .brand-dot{width:10px;height:10px;border-radius:50%;background:var(--brand-blue)}
  .brand-tagline{font-family:"Arimo",sans-serif;font-weight:400}
  .panel--front .brand{left:170px;width:210px;top:64px}
  .panel--front .brand-name{font-size:19px}
  .panel--front .brand-tagline{font-size:13px;margin-top:1px}
  .panel--side .brand{left:0;width:304px;top:118px}
  .panel--side .brand-name{font-size:24px}
  .panel--side .brand-tagline{font-size:17px;margin-top:2px}

  .service-badge{display:block}
  .panel--front .service-badge{left:220px;top:130px;width:150px;height:100px}
  .panel--side .service-badge{left:30px;top:350px;width:260px;height:175px}

  .product-heading{left:233px;top:571px;color:var(--brand-blue)}
  .product-heading .kicker{font-family:"Montserrat",sans-serif;font-weight:800;font-size:12px;color:var(--ink)}
  .product-heading .title{
    font-family:"Montserrat",sans-serif;font-weight:900;font-size:22px;line-height:22px;
    color:var(--brand-blue);text-shadow:0 0 0 var(--white),1px 1px 0 var(--white),-1px -1px 0 var(--white),1px -1px 0 var(--white),-1px 1px 0 var(--white);
    margin-top:3px;
  }
  .contact{left:236px;top:672px;color:var(--ink)}
  .contact-cta{font-family:"Montserrat",sans-serif;font-weight:800;font-size:12.5px}
  .contact-phone{display:flex;align-items:center;gap:5px;font-family:"Montserrat",sans-serif;font-weight:800;font-size:17px;color:var(--brand-blue);margin-top:3px}
  .contact-phone svg{width:17px;height:17px}
  .contact-email{font-size:9px;font-weight:700;margin-top:3px}
  .contact-social{display:flex;align-items:center;gap:4px;font-size:9px;font-weight:700;margin-top:5px}
  .contact-social .dot{width:8px;height:8px;border-radius:50%;background:var(--ink)}

  .filtration-pill{
    display:flex;align-items:center;gap:6px;border-radius:22px;
    background:var(--blue-mid);color:var(--white);
    font-family:"Montserrat",sans-serif;font-weight:800;text-transform:uppercase;
  }
  .filtration-pill .pill-icon{flex:none;border-radius:50%;background:var(--white);display:flex;align-items:center;justify-content:center}
  .panel--front .filtration-pill{left:194px;top:769px;width:160px;height:42px;padding:0 8px;font-size:8.5px;line-height:9.5px}
  .panel--front .pill-icon{width:28px;height:28px}
  .panel--side .filtration-pill{left:24px;top:820px;width:134px;height:36px;padding:0 6px;font-size:7.5px;line-height:8.5px}
  .panel--side .pill-icon{width:24px;height:24px}

  .water-list{list-style:none;color:var(--white)}
  .water-list li{display:flex;align-items:center;gap:6px}
  .water-list li::before{
    content:"✓";display:inline-flex;align-items:center;justify-content:center;
    border:1px solid var(--white);border-radius:50%;font-size:7px;font-weight:700;
  }
  .panel--front .water-list{left:199px;top:829px;font-size:11px}
  .panel--front .water-list li{height:16px}
  .panel--front .water-list li::before{width:9px;height:9px}
  .panel--side .water-list{left:26px;top:865px;font-size:9.5px}
  .panel--side .water-list li{height:13.4px}
  .panel--side .water-list li::before{width:8px;height:8px;font-size:6px}
</style>
</head>
<body>

<h2 class="view-label view-label--front">FRONT DESIGN</h2>
<h2 class="view-label view-label--side">SIDE DESIGN</h2>

<!-- Front panel -->
<section class="panel panel--front">
  <svg class="panel-art" viewBox="0 0 389 972" preserveAspectRatio="none">
    <defs>
      <radialGradient id="frontGlow" cx="260" cy="330" r="420" gradientUnits="userSpaceOnUse">
        <stop offset="0" stop-color="#ffffff"/>
        <stop offset="0.25" stop-color="#a9d8f6"/>
        <stop offset="0.6" stop-color="#3b96df"/>
        <stop offset="1" stop-color="#0d5fb5"/>
      </radialGradient>
      <linearGradient id="frontPhoto" x1="0" y1="0" x2="1" y2="1">
        <stop offset="0" stop-color="#e8e1dc"/>
        <stop offset="0.5" stop-color="#c9b2a4"/>
        <stop offset="1" stop-color="#6f5d56"/>
      </linearGradient>
      <linearGradient id="frontBottle" x1="0" y1="0" x2="1" y2="0">
        <stop offset="0" stop-color="#5fb2e6"/>
        <stop offset="0.5" stop-color="#bfe6fb"/>
        <stop offset="1" stop-color="#3f93d3"/>
      </linearGradient>
      <linearGradient id="frontSplash" x1="0" y1="0" x2="1" y2="0">
        <stop offset="0" stop-color="#e6f5fd" stop-opacity="0.9"/>
        <stop offset="1" stop-color="#e6f5fd" stop-opacity="0"/>
      </linearGradient>
    </defs>
    <rect width="389" height="972" fill="url(#frontGlow)"/>
    <path d="M0 0H389V110C360 170 300 215 220 232C140 248 60 246 0 240Z" fill="#ffffff"/>
    <g role="img" aria-label="Photo of a young woman drinking a glass of water with water splash">
      <path d="M0 0H215C230 80 220 180 200 245C130 250 60 250 0 245Z" fill="url(#frontPhoto)"/>
      <path d="M0 0H40V120H0Z" fill="#d8eefa" opacity="0.7"/>
    </g>
    <path d="M0 236C90 250 200 245 280 225C330 212 365 190 389 160V185C360 215 320 235 270 248C190 266 90 266 0 258Z" fill="#7fcdef"/>
    <path d="M0 258C90 266 190 266 270 248C320 236 360 215 389 185V215C350 248 280 262 200 268C120 274 50 270 0 272Z" fill="#0b53ab"/>
    <!-- cabinet cut-outs -->
    <g fill="none" stroke="#ffffff" stroke-width="1.2">
      <rect x="52" y="273" width="133" height="75"/>
      <rect x="13" y="383" width="195" height="317"/>
      <rect x="30" y="401" width="162" height="281"/>
      <rect x="269" y="330" width="83" height="205"/>
      <rect x="356" y="443" width="24" height="50"/>
    </g>
    <rect role="img" aria-label="Water splash" x="0" y="700" width="220" height="110" fill="url(#frontSplash)"/>
    <path d="M0 770C100 745 200 750 275 740C320 733 360 722 389 712V740C350 752 300 762 250 766C160 772 80 775 0 790Z" fill="#8fd4f1"/>
    <path d="M0 790C80 775 160 772 250 766C300 762 350 752 389 740V972H0Z" fill="#0b55ad"/>
    <rect role="img" aria-label="Large blue water bottle" x="40" y="728" width="118" height="240" rx="16" fill="url(#frontBottle)"/>
  </svg>

  <div class="brand">
    <div class="brand-name"><span class="brand-dot"></span>CEDAR HOLLOW</div>
    <div class="brand-tagline">Purified Spring Water</div>
  </div>

  <svg class="service-badge" viewBox="0 0 260 175" aria-label="24 hours self service">
    <path d="M110 78A48 48 0 1 0 30 96" fill="none" stroke="#17439a" stroke-width="7"/>
    <path d="M30 96A48 48 0 0 0 100 112" fill="none" stroke="#17439a" stroke-width="3" stroke-dasharray="4 3"/>
    <path d="M98 70L124 80L102 95Z" fill="#17439a"/>
    <text x="64" y="70" text-anchor="middle" font-family="Montserrat,sans-serif" font-weight="900" font-style="italic" font-size="40" fill="#17439a">24</text>
    <text x="64" y="88" text-anchor="middle" font-family="Montserrat,sans-serif" font-weight="800" font-style="italic" font-size="12" fill="#17439a">HOURS</text>
    <text x="250" y="124" text-anchor="end" font-family="Montserrat,sans-serif" font-weight="900" font-style="italic" font-size="46" fill="#17439a" stroke="#ffffff" stroke-width="1.5" paint-order="stroke">SELF</text>
    <text x="250" y="168" text-anchor="end" font-family="Montserrat,sans-serif" font-weight="900" font-style="italic" font-size="46" fill="#17439a" stroke="#ffffff" stroke-width="1.5" paint-order="stroke">SERVICE</text>
  </svg>

  <div class="product-heading">
    <div class="kicker">CEDAR HOLLOW</div>
    <div class="title">PURIFIED<br>DRINKING<br>WATER</div>
  </div>

  <div class="contact">
    <div class="contact-cta">CALL US TODAY</div>
    <div class="contact-phone">
      <svg viewBox="0 0 20 20"><circle cx="10" cy="10" r="10" fill="#1260b8"/><path d="M6.5 5.5l2 0 .8 2.5-1.2 1a6 6 0 0 0 3 3l1-1.2 2.5.8v2c0 .6-.5 1-1 1A9 9 0 0 1 5.5 6.5c0-.5.4-1 1-1z" fill="#fff"/></svg>
      00 5678 90
    </div>
    <div class="contact-email">Email: info@cedarhollow.com</div>
    <div class="contact-social"><span class="dot"></span>/cedarhollow</div>
  </div>

  <div class="filtration-pill">
    <span class="pill-icon"><svg width="16" height="16" viewBox="0 0 16 16"><path d="M8 2C6 5 4.5 7 4.5 9.5a3.5 3.5 0 0 0 7 0C11.5 7 10 5 8 2z" fill="#1f7fd2"/></svg></span>
    <span>Passed 6 stages of water filtration process</span>
  </div>

  <ul class="water-list">
    <li>High Purity Water</li>
    <li>Alkaline Water</li>
    <li>Distilled Water</li>
    <li>Mineral Enhanced Water</li>
    <li>Alkaline Iodized Water</li>
    <li>Bottled Water and More...</li>
  </ul>
</section>

<!-- Side panel -->
<section class="panel panel--side">
  <svg class="panel-art" viewBox="0 0 304 972" preserveAspectRatio="none">
    <defs>
      <radialGradient id="sideGlow" cx="160" cy="330" r="380" gradientUnits="userSpaceOnUse">
        <stop offset="0" stop-color="#ffffff"/>
        <stop offset="0.25" stop-color="#aad9f6"/>
        <stop offset="0.6" stop-color="#3b96df"/>
        <stop offset="1" stop-color="#0d5fb5"/>
      </radialGradient>
      <linearGradient id="sidePhoto" x1="0" y1="0" x2="1" y2="1">
        <stop offset="0" stop-color="#e6ddd6"/>
        <stop offset="0.5" stop-color="#c7ae9f"/>
        <stop offset="1" stop-color="#6d5b54"/>
      </linearGradient>
      <linearGradient id="sideBottle" x1="0" y1="0" x2="1" y2="0">
        <stop offset="0" stop-color="#5fb2e6"/>
        <stop offset="0.5" stop-color="#bfe6fb"/>
        <stop offset="1" stop-color="#3f93d3"/>
      </linearGradient>
      <linearGradient id="sideSplash" x1="1" y1="0" x2="0" y2="0">
        <stop offset="0" stop-color="#e6f5fd" stop-opacity="0.9"/>
        <stop offset="1" stop-color="#e6f5fd" stop-opacity="0"/>
      </linearGradient>
    </defs>
    <rect width="304" height="972" fill="url(#sideGlow)"/>
    <path d="M0 0H304V165C230 210 130 232 0 232Z" fill="#ffffff"/>
    <path d="M0 232C130 232 230 210 304 165V195C230 242 130 262 0 262Z" fill="#8fd4f1"/>
    <path d="M0 262C130 262 230 242 304 195V228C220 278 120 292 0 300Z" fill="#0b53ab"/>
    <rect role="img" aria-label="Water splash" x="150" y="520" width="154" height="200" fill="url(#sideSplash)"/>
    <rect role="img" aria-label="Photo of a young woman drinking a glass of water" x="16" y="555" width="240" height="250" rx="30" fill="url(#sidePhoto)"/>
    <path d="M0 800C90 790 180 775 240 770C270 768 290 765 304 760V972H0Z" fill="#0b55ad"/>
    <rect role="img" aria-label="Large blue water bottle" x="190" y="765" width="97" height="185" rx="14" fill="url(#sideBottle)"/>
  </svg>

  <div class="brand">
    <div class="brand-name"><span class="brand-dot"></span>CEDAR HOLLOW</div>
    <div class="brand-tagline">Purified Spring Water</div>
  </div>

  <svg class="service-badge" viewBox="0 0 260 175" aria-label="24 hours self service">
    <path d="M110 78A48 48 0 1 0 30 96" fill="none" stroke="#17439a" stroke-width="7"/>
    <path d="M30 96A48 48 0 0 0 100 112" fill="none" stroke="#17439a" stroke-width="3" stroke-dasharray="4 3"/>
    <path d="M98 70L124 80L102 95Z" fill="#17439a"/>
    <text x="64" y="70" text-anchor="middle" font-family="Montserrat,sans-serif" font-weight="900" font-style="italic" font-size="40" fill="#17439a">24</text>
    <text x="64" y="88" text-anchor="middle" font-family="Montserrat,sans-serif" font-weight="800" font-style="italic" font-size="12" fill="#17439a">HOURS</text>
    <text x="250" y="124" text-anchor="end" font-family="Montserrat,sans-serif" font-weight="900" font-style="italic" font-size="46" fill="#17439a" stroke="#ffffff" stroke-width="1.5" paint-order="stroke">SELF</text>
    <text x="250" y="168" text-anchor="end" font-family="Montserrat,sans-serif" font-weight="900" font-style="italic" font-size="46" fill="#17439a" stroke="#ffffff" stroke-width="1.5" paint-order="stroke">SERVICE</text>
  </svg>

  <div class="filtration-pill">
    <span class="pill-icon"><svg width="14" height="14" viewBox="0 0 16 16"><path d="M8 2C6 5 4.5 7 4.5 9.5a3.5 3.5 0 0 0 7 0C11.5 7 10 5 8 2z" fill="#1f7fd2"/></svg></span>
    <span>Passed 6 stages of water filtration process</span>
  </div>

  <ul class="water-list">
    <li>High Purity Water</li>
    <li>Alkaline Water</li>
    <li>Distilled Water</li>
    <li>Mineral Enhanced Water</li>
    <li>Alkaline Iodized Water</li>
    <li>Bottled Water and More...</li>
  </ul>
</section>

</body>
</html>
```